Rack card for a integrative medical practice

Need an eye-catching rack card with our logo with content as provided. We have a membership based holistic medical practice which incorporates western and holistic medicine. We would like to focus on wellness and healthy lifestyle. See uploaded files for what is included in the membership. Would like 2 page rack card color on both sides. Logo must be on the front.

Target Market(s)

People looking for alternative medicine, healthy lifestyle.

Industry/Entity Type

Health and Wellness

Colors
00AB8E
00BBA5
67D7C9
C6EFE9
E9F9F6

Requirements
Must have
• Must spark interest at first sight. Clear message.
Nice to have
• Warm, bright and positive vibe. Organic, neutral and earthy colors.
Should not have
• Traditional medical practice vibe (cold, formal, industrial). No PINK except the logo.

```html
<!DOCTYPE html>
<html lang="en">
<head>
<meta charset="utf-8">
<title>Lumen Health &amp; Wellness – Rack Card</title>
<link rel="stylesheet" href="https://fonts.googleapis.com/css2?family=Amaranth:wght@400;700&family=Federo&display=swap">
<style>
  :root {
    --teal: #00ab8e;
    --teal-bright: #00bba5;
    --teal-soft: #67d7c9;
    --mint: #c6efe9;
    --mist: #e9f9f6;
    --teal-deep: #00806b;
    --ink: #111111;
    --pine: #1f3b33;
    --sand: #efe6d6;
    --white: #ffffff;
  }
  * { box-sizing: border-box; margin: 0; padding: 0; }
  html, body {
    width: 1200px; height: 1057px; overflow: hidden;
    background: var(--white);
    font-family: "Amaranth", sans-serif;
  }
  .canvas { position: relative; width: 1200px; height: 1057px; }

  .card {
    position: absolute;
    overflow: hidden;
    background: linear-gradient(160deg, #f7fcfb 0%, var(--mist) 55%, #dff3ef 100%);
  }
  .corner-bloom {
    position: absolute; top: 0; right: 0;
    width: 170px; height: 120px;
    background: radial-gradient(ellipse at 70% 30%, var(--sand) 0%, rgba(239,230,214,0.6) 45%, rgba(239,230,214,0) 75%);
  }

  /* Front */
  .card--front { left: 59px; top: 154px; width: 538px; height: 847px; }
  .front__title {
    position: absolute; top: 30px; left: 0; width: 100%;
    text-align: center; color: var(--teal);
    font-size: 57px; line-height: 64px; font-weight: 400;
    text-shadow: 1px 2px 2px rgba(0,0,0,0.15);
  }
  .front__tagline {
    position: absolute; top: 222px; left: 0; width: 100%;
    text-align: center; color: var(--ink);
    font-size: 38px; line-height: 52px;
  }
  .front__tagline em { font-style: normal; color: var(--teal); }
  .front__rule {
    position: absolute; top: 446px; left: 0; width: 100%; height: 6px;
    background: var(--teal);
  }
  .front__photo {
    position: absolute; top: 452px; left: 0; width: 100%; height: 302px;
    background: linear-gradient(180deg, #eef4f1 0%, #d6ddd6 45%, #bcb6a8 75%, #e4e3d8 100%);
  }
  .front__brand {
    position: absolute; top: 474px; left: 0; width: 100%;
    display: flex; justify-content: center; align-items: center; gap: 10px;
  }
  .front__brand .brand__dot { width: 14px; height: 14px; }
  .front__brand .brand__name { font-size: 32px; letter-spacing: 7px; }
  .front__base-line {
    position: absolute; top: 754px; left: 0; width: 100%; height: 4px;
    background: var(--teal-deep);
  }
  .front__address {
    position: absolute; top: 758px; left: 0; width: 100%; height: 89px;
    background: var(--teal);
    color: var(--white); text-align: center;
    font-size: 27px; line-height: 36px; padding-top: 10px;
  }

  /* Back */
  .card--back { left: 597px; top: 57px; width: 538px; height: 847px; }
  .back__heading {
    position: absolute; top: 26px; left: 0; width: 100%;
    text-align: center; color: var(--ink);
    font-family: "Federo", sans-serif; font-weight: 400;
    font-size: 43px; line-height: 50px; letter-spacing: 1px;
  }
  .benefits {
    position: absolute; top: 164px; left: 4px; right: 4px;
    list-style: none;
    color: var(--teal-deep); font-size: 25.5px; line-height: 38.4px;
  }
  .benefits li { position: relative; padding-left: 24px; white-space: nowrap; }
  .benefits li::before {
    content: ""; position: absolute; left: 0; top: 13px;
    border-left: 8px solid var(--ink);
    border-top: 6px solid transparent; border-bottom: 6px solid transparent;
  }
  .benefits .value { color: var(--ink); }
  .back__photo {
    position: absolute; left: 0; bottom: 0; width: 100%; height: 230px;
    background: linear-gradient(180deg, rgba(233,249,246,0) 0%, rgba(198,239,233,0.7) 45%, #b9e3dc 100%);
  }
  .brand {
    display: flex; justify-content: center; align-items: center; gap: 14px;
  }
  .back__brand { position: absolute; top: 660px; left: 0; width: 100%; }
  .brand__dot { width: 18px; height: 18px; border-radius: 50%; background: var(--teal); }
  .brand__name { color: var(--pine); font-size: 46px; letter-spacing: 10px; }
</style>
</head>
<body>
<main class="canvas">

  <section class="card card--front">
    <div class="corner-bloom" role="img" aria-label="Soft cream dried flowers in the corner"></div>
    <h1 class="front__title">Lumen Health &amp;<br>Wellness</h1>
    <p class="front__tagline">A Direct<br>Primary Care Practice<br>Focused on a<br>More <em>HOLISTIC</em></p>
    <div class="front__rule"></div>
    <div class="front__photo" role="img" aria-label="Photo of a person meditating beside candles, a reed diffuser and stacked stones"></div>
    <div class="brand front__brand">
      <span class="brand__dot"></span>
      <span class="brand__name">LUMEN</span>
    </div>
    <div class="front__base-line"></div>
    <p class="front__address">1420 W Elm Ave., STE 2B<br>Brookfield</p>
  </section>

  <section class="card card--back">
    <div class="corner-bloom" role="img" aria-label="Soft cream dried flowers in the corner"></div>
    <h2 class="back__heading">WHAT'S INCLUDED IN<br>YOUR MEMBERSHIP :</h2>
    <ul class="benefits">
      <li>Unlimited office visits with no copay</li>
      <li>Direct communication with your doctor</li>
      <li>Discounted labs, imaging and medications</li>
      <li>Free initial acupuncture session (<span class="value">$250 value</span>).</li>
      <li>2 Vitalscan testings per year (<span class="value">$100 value</span>)</li>
      <li>Discounts for supplements and health<br>products in the clinic</li>
      <li>Discounts for iv vitamin infusion therapy</li>
      <li>Personalized nutrition plan after advanced<br>testing such as gut microbiome, hormonal,<br>metabolism test, etc.</li>
    </ul>
    <div class="back__photo" role="img" aria-label="Faint photo of an acupuncture treatment on a back"></div>
    <div class="brand back__brand">
      <span class="brand__dot"></span>
      <span class="brand__name">LUMEN</span>
    </div>
  </section>

</main>
</body>
</html>
```